Sleek, Professional Business Card Design Needed

Business Cards - Logo Attached.

We are a solar consulting company. We are national and want our cards to represent the professional high quality products that we offer.

Industry/Entity Type

Business

Contact Information for Business Card

n/a

Requirements
Must have
• Design
• Name
• Position
• Number
• Email
• Address
Should not have
• Not be too crowded

```html
<!DOCTYPE html>
<html lang="en">
<head>
<meta charset="utf-8">
<title>Bright Field Solar – Business Card</title>
<link href="https://fonts.googleapis.com/css2?family=Open+Sans:wght@400;600;800&display=swap" rel="stylesheet">
<style>
  :root{
    --stage:#e8e9eb;
    --card-white:#ffffff;
    --brand-blue:#0b8dcc;
    --brand-green:#8dc63f;
    --text-light:#ffffff;
  }
  *{box-sizing:border-box;margin:0;padding:0}
  html,body{width:1200px;height:750px;overflow:hidden;background:var(--stage)}
  body{font-family:"Open Sans",Arial,sans-serif;position:relative}

  .card{
    position:absolute;left:410px;top:42px;
    width:380px;height:665px;border-radius:34px;overflow:hidden;
    background:var(--brand-blue);
    box-shadow:0 10px 30px rgba(0,0,0,.18);
  }
  .card__brand{
    position:absolute;left:0;top:0;width:100%;height:230px;
    background:var(--card-white);
    display:flex;flex-direction:column;align-items:center;justify-content:center;gap:14px;
  }
  .brand__mark{width:64px;height:64px;border-radius:50%;border:7px solid var(--brand-blue)}
  .brand__name{
    font-weight:600;font-size:25px;letter-spacing:1px;color:var(--brand-green);
    text-transform:uppercase;
  }

  .card__identity{position:absolute;left:34px;top:262px;color:var(--text-light)}
  .identity__name{font-weight:800;font-size:31px;letter-spacing:.5px;text-transform:uppercase;line-height:1.1}
  .identity__role{font-weight:400;font-size:15px;text-transform:uppercase;margin-top:4px;letter-spacing:.3px}

  .contact-rule{
    position:absolute;left:0;width:100%;height:9px;background:var(--brand-green);
  }
  .contact-icon{
    position:absolute;left:28px;width:36px;height:36px;
    background:var(--brand-green);transform:rotate(45deg);
    display:flex;align-items:center;justify-content:center;
  }
  .contact-icon svg{transform:rotate(-45deg);width:18px;height:18px}
  .contact-text{
    position:absolute;left:34px;color:var(--text-light);
    font-size:17px;line-height:1.35;font-weight:400;
  }
</style>
</head>
<body>
  <article class="card">
    <header class="card__brand">
      <span class="brand__mark"></span>
      <span class="brand__name">Bright Field Solar</span>
    </header>

    <div class="card__identity">
      <h1 class="identity__name">Daniel Rourke</h1>
      <p class="identity__role">Creative Head</p>
    </div>

    <!-- phone -->
    <div class="contact-rule" style="top:376px"></div>
    <div class="contact-icon" style="top:362px">
      <svg viewBox="0 0 24 24" fill="#fff"><path d="M6.6 10.8a15.1 15.1 0 0 0 6.6 6.6l2.2-2.2a1 1 0 0 1 1-.25 11.4 11.4 0 0 0 3.6.57 1 1 0 0 1 1 1V20a1 1 0 0 1-1 1A17 17 0 0 1 3 4a1 1 0 0 1 1-1h3.5a1 1 0 0 1 1 1c0 1.25.2 2.45.57 3.57a1 1 0 0 1-.25 1z"/></svg>
    </div>
    <p class="contact-text" style="top:404px">(021) 555 - 987 - 6543<br>(021) 555 - 987 - 6543</p>

    <!-- web -->
    <div class="contact-rule" style="top:461px"></div>
    <div class="contact-icon" style="top:447px">
      <svg viewBox="0 0 24 24" fill="none" stroke="#fff" stroke-width="2"><circle cx="12" cy="12" r="9"/><path d="M3 12h18M12 3c3 3 3 15 0 18M12 3c-3 3-3 15 0 18"/></svg>
    </div>
    <p class="contact-text" style="top:489px">info@brightfieldsolar.com<br>www.brightfieldsolar.com</p>

    <!-- address -->
    <div class="contact-rule" style="top:551px"></div>
    <div class="contact-icon" style="top:537px">
      <svg viewBox="0 0 24 24" fill="#fff"><path d="M12 2a7 7 0 0 0-7 7c0 5.2 7 13 7 13s7-7.8 7-13a7 7 0 0 0-7-7zm0 9.5A2.5 2.5 0 1 1 12 6.5a2.5 2.5 0 0 1 0 5z"/></svg>
    </div>
    <p class="contact-text" style="top:579px">Sunridge Plaza Main<br>Road 5678 - USA</p>
  </article>
</body>
</html>
```